GPS Tracker Business Card Design

We need a business card for a GPS Vehicle tracking company. We sell the hardware for the vehicle and the software platform to monitor your vehicle/s. Including high asset non-powered vehicles like a trailer using our solar powered unit.
We like using dark blue to different shades of blue along with gold. We have phone apps for Android and Apple devices.

We have a platform for families wanting to track their teenage driver and children; Plus a Fleet vehicle tracking platform.

Features: unlimited number of vehicles and/or assets including snow mobiles forklifts generators trailers airport equipment

Reports for driving behavior reports and alerts dashboard fleet maintenace timeline view and replay geofence real time alerts logbook scheduling route optimization accounting integration fleet grouping closest vehicle locator On Board Diagnostics.

Benefits: Increased productivity improved fuel efficiency organizing your business improve time management simplify back end processes, reduce fleet fuel efficiency and expenses increase fleet security etc..

Please view website: Velmora.com

Industry/Entity Type

Business

Contact Information for Business Card

Harold B Pennick

```html
<!DOCTYPE html>
<html lang="en">
<head>
<meta charset="utf-8">
<title>Velmora Business Card</title>
<link href="https://fonts.googleapis.com/css2?family=Open+Sans:wght@400;600;700;800&display=swap" rel="stylesheet">
<style>
  :root {
    --page: #e9e7e3;
    --card-top: #2a2c30;
    --card-bottom: #121315;
    --ink-light: #e6e8ea;
    --ink-muted: #9a9ea3;
    --globe-deep: #1b2a44;
    --globe-mid: #2f4f78;
    --globe-light: #4f86b8;
    --gold: #f2cc62;
    --gold-text: #f5c94a;
    --tag-ink: #1f5fa8;
  }
  * { box-sizing: border-box; margin: 0; padding: 0; }
  html, body { width: 1200px; height: 1023px; overflow: hidden; }
  body {
    background: var(--page);
    font-family: "Open Sans", Arial, sans-serif;
    position: relative;
  }
  .card {
    position: absolute;
    left: 270px;
    width: 660px;
    height: 377px;
    border-radius: 6px;
    overflow: hidden;
    background: linear-gradient(160deg, var(--card-top) 0%, var(--card-bottom) 75%);
    box-shadow: 0 14px 30px rgba(0,0,0,0.28);
  }
  .card--front { top: 90px; }
  .card--back { top: 547px; }

  .globe {
    position: absolute;
    left: 0; top: 0;
    width: 660px; height: 377px;
  }
  .wordmark {
    font-weight: 600;
    color: var(--ink-light);
    line-height: 1;
  }
  .tagline {
    font-weight: 400;
    color: var(--ink-muted);
    line-height: 1;
  }
  .card--front .brand {
    position: absolute;
    left: 40px; top: 214px;
  }
  .card--front .wordmark { font-size: 62px; }
  .card--front .tagline { font-size: 17px; margin-top: 14px; }

  .name-tag {
    position: absolute;
    left: 330px; top: 48px;
    width: 196px; height: 78px;
    background: var(--gold);
    border-radius: 5px;
    text-align: center;
    padding-top: 14px;
  }
  .name-tag .person {
    font-size: 19px;
    font-weight: 600;
    color: var(--tag-ink);
    line-height: 1.2;
  }
  .name-tag .role {
    font-size: 13px;
    color: #333;
    margin-top: 4px;
  }
  .pin {
    position: absolute;
    left: 410px; top: 150px;
    width: 34px; height: 44px;
  }

  .card--back .brand {
    position: absolute;
    left: 200px; top: 56px;
  }
  .card--back .wordmark { font-size: 76px; }
  .card--back .tagline { font-size: 19px; margin-top: 16px; }
  .contact {
    position: absolute;
    left: 150px; top: 226px;
  }
  .phone {
    font-size: 40px;
    font-weight: 800;
    color: var(--gold-text);
    letter-spacing: 1px;
    line-height: 1;
  }
  .cta {
    font-size: 22px;
    color: #fff;
    margin-top: 14px;
  }
  .cta strong { font-weight: 700; }
</style>
</head>
<body>

  <section class="card card--front">
    <svg class="globe" viewBox="0 0 660 377" role="img" aria-label="Dotted world map on a blue globe">
      <defs>
        <radialGradient id="globe-fill" cx="70%" cy="40%" r="70%">
          <stop offset="0%" stop-color="var(--globe-light)"/>
          <stop offset="55%" stop-color="var(--globe-mid)"/>
          <stop offset="100%" stop-color="var(--globe-deep)"/>
        </radialGradient>
      </defs>
      <circle cx="760" cy="470" r="480" fill="url(#globe-fill)" opacity="0.9"/>
    </svg>

    <div class="brand">
      <div class="wordmark">Velmora</div>
      <div class="tagline">Always Know Where Your Fleet Is</div>
    </div>

    <div class="name-tag">
      <div class="person">Harold B Pennick</div>
      <div class="role">Director</div>
    </div>

    <svg class="pin" viewBox="0 0 34 44" aria-hidden="true">
      <path d="M17 1C8.2 1 1 8 1 16.6 1 28 17 43 17 43s16-15 16-26.4C33 8 25.8 1 17 1z" fill="var(--gold)"/>
      <circle cx="17" cy="16" r="6" fill="#1a1c1f"/>
    </svg>
  </section>

  <section class="card card--back">
    <div class="brand">
      <div class="wordmark">Velmora</div>
      <div class="tagline">Always Know Where Your Fleet Is</div>
    </div>
    <div class="contact">
      <div class="phone">866-555-0147</div>
      <div class="cta">Call today for a <strong>Free demo</strong></div>
    </div>
  </section>

</body>
</html>
```